Tovlen Systems New Website - IT Infrastructure | Smart Cabinet | Micro Data Center

We're an IT SI providing Server Room Design & Build | All-in-One Rack & Smart Cabinet | Structured Cabling | IT Relocation | Maintenance. Old website can be found at www.tovlensys.com.hk. We'd like a brand new wix website which is modern, minimalist, interactive with some animation. Website content will be mostly static and include our service, our project, news and events, about us, contacts, blogs, partners and brands, etc.

reference sites:
We'd like to see more designs referring to below

https://www.pixelbazar.example/design/51730264
https://www.pixelbazar.example/design/51869047
https://vellhorn.example/

Animation (scrolling effect) referring to
https://vellhorn.example/intelligence/smart-office-room/
Updates

we'd like below style.

Designs look the same

Target Market(s)

Commercials in HK

Industry/Entity Type

IT, Technology, Data Center

Coding

Coded - Design and coding required

Font styles to use
Sans Serif

Requirements
Must have
• CMS, Some Interactive Elements/ Graphics

```html
<!DOCTYPE html>
<html lang="en">
<head>
<meta charset="utf-8">
<title>Tovlen Systems – Website Design</title>
<link href="https://fonts.googleapis.com/css2?family=Roboto:wght@400;500;700&family=Lato:wght@400;700&display=swap" rel="stylesheet">
<style>
:root{
  --stage:#ececee;
  --navy:#151b34;
  --ink:#1b2240;
  --red:#d2341f;
  --light:#f3f3f3;
  --white:#ffffff;
  --muted:#8a8f9c;
  --footer:#1d1d1f;
  --photo-a:#2d3350;
  --photo-b:#6a7088;
}
*{margin:0;padding:0;box-sizing:border-box}
html,body{width:1177px;height:1200px;overflow:hidden;background:var(--stage)}
body{position:relative;font-family:"Lato",sans-serif;color:var(--ink)}
.abs{position:absolute}
.page{position:absolute;overflow:hidden;box-shadow:0 6px 24px rgba(20,25,50,.12)}
.page-right{left:572px;top:0;width:472px;height:1125px;background:var(--white)}
.page-left{left:132px;top:75px;width:488px;height:1125px;background:var(--white)}
.section{position:absolute;left:0;width:100%}
.dark{background:var(--navy);color:var(--white)}
.grey{background:var(--light)}
.tag{position:absolute;left:0;width:100%;text-align:center;font-size:3.6px;color:var(--ink)}
.tag span{display:inline-block;background:#e4e5ea;padding:.6px 2px;border-left:1px solid var(--red)}
.dark .tag span,.tag.on-dark span{background:rgba(255,255,255,.12);color:#fff}
.tag.left{text-align:left}
.title{position:absolute;left:0;width:100%;text-align:center;font-family:"Roboto",sans-serif;font-weight:500;font-size:16px;color:var(--ink);line-height:1.1}
.title em{font-style:normal;color:var(--red)}
.btn{position:absolute;background:var(--red);color:#fff;font-size:3.8px;font-weight:700;display:flex;align-items:center;justify-content:center}
.btn.outline{background:#fff;color:var(--red);border:.6px solid var(--red)}
.photo{position:absolute;background:linear-gradient(160deg,var(--photo-b),var(--photo-a))}
.photo.warm{background:linear-gradient(150deg,#c9a2b6,#8d8a95 45%,#e8e2d6)}
.photo.hall{background:linear-gradient(180deg,#3b4466 0%,#56607f 45%,#6f7590 100%)}
.logo{position:absolute;display:flex;align-items:center;gap:2px;font-family:"Roboto",sans-serif;font-weight:500;color:#fff}
.logo i{display:block;border:1.2px solid #fff}
.check li{list-style:none;position:relative;padding-left:13px;font-size:3.8px;color:#c4c7d2;height:9.6px}
.check li::before{content:"";position:absolute;left:2px;top:.6px;width:2.4px;height:1.3px;border-left:.7px solid var(--red);border-bottom:.7px solid var(--red);transform:rotate(-45deg)}
.small{font-size:3.7px;line-height:1.45;color:var(--muted)}

/* projects */
.card{position:absolute;background:#fff;box-shadow:0 0 2px rgba(0,0,0,.12)}
.card .photo{left:0;top:0;width:100%}
.card p{position:absolute;left:4px;right:3px;font-size:5px;line-height:1.3;color:#333}
.card .btn{left:4px;right:4px;height:12px}
.card.active{box-shadow:0 2px 6px rgba(0,0,0,.2)}

/* news */
.news-item{position:absolute;left:0;width:100%}
.news-item .date{position:absolute;font-size:3.4px;color:#9a9ea8}
.news-item h4{position:absolute;font-size:5px;font-weight:400;color:var(--ink)}
.news-item .small{position:absolute}
.news-item .more{position:absolute;font-size:3.5px;color:var(--red)}

/* hero */
.hero{background:linear-gradient(100deg,#141c40 0%,#1c2550 45%,#232a45 70%,#3a3f52 100%)}
.nav{position:absolute;top:21px;font-size:4.4px;color:#fff;display:flex;gap:0}
.nav span{position:absolute;white-space:nowrap}

/* features */
.feature{position:absolute;width:120px}
.feature svg{position:absolute;left:0;top:0}
.feature h5{position:absolute;left:24px;top:0;font-size:5px;font-weight:700;color:var(--ink);white-space:nowrap}
.feature p{position:absolute;left:24px;top:8px;width:82px}

/* services */
.service{position:absolute;top:74px;width:103px;height:58px;background:var(--light)}
.service b{position:absolute;left:16px;top:12px;font-family:"Roboto",sans-serif;font-weight:400;font-size:11px;color:var(--red)}
.service p{position:absolute;left:16px;top:33px;font-size:5.4px;line-height:1.5;color:#555}
.service.active{background:var(--red)}
.service.active b,.service.active p{color:#fff}

/* contact */
.field{position:absolute;left:251px;width:129px;border:.6px solid #9aa0b5;font-size:3.6px;color:#e6e8ef;padding:4px 5px}
.footer-col h6{font-size:4.2px;font-weight:700;color:#fff;margin-bottom:5px}
.footer-col p{font-size:3.1px;color:#a5a7ad;line-height:1.35;margin-bottom:4px}
.partners span{font-family:"Roboto",sans-serif;font-weight:500;font-size:9px;color:#8c8f96}
</style>
</head>
<body>

<!-- RIGHT PAGE -->
<div class="page page-right">

  <section class="section dark" style="top:0;height:135px">
    <div class="photo warm" style="left:96px;top:3px;width:101px;height:97px" role="img" aria-label="Miniature workers with a network cable connector"></div>
    <div class="abs" style="left:247px;top:4px;font-size:4.8px;font-weight:700">Tovlen’s solution at-a-glance includes;</div>
    <ul class="check abs" style="left:247px;top:18px">
      <li>Data Center / Server Room Design and Build</li>
      <li>Structured Cabling Solution</li>
      <li>Data and Voice Networks, IP-Telephony Solution</li>
      <li>WiFi Solution</li>
      <li>Relocation and Migration Service</li>
      <li>AV and Conference Room System</li>
    </ul>
    <div class="btn" style="left:247px;top:86px;width:50px;height:15px">Explore More</div>
  </section>

  <section class="section" style="top:135px;height:189px">
    <div class="tag" style="top:28px"><span>What We Have Done</span></div>
    <div class="title" style="top:40px">Our <em>Projects</em></div>
    <div class="card" style="left:79px;top:67px;width:77px;height:83px">
      <div class="photo hall" style="height:40px" role="img" aria-label="Empty data hall"></div>
      <p style="top:47px">A renowned China based listed insurance company</p>
      <div class="btn outline" style="top:67px">Explore More</div>
    </div>
    <div class="card active" style="left:158px;top:67px;width:77px;height:83px">
      <div class="photo hall" style="height:40px" role="img" aria-label="Empty data hall"></div>
      <p style="top:47px">Worldmart Sourcing</p>
      <div class="btn" style="top:67px">Explore More</div>
    </div>
    <div class="card" style="left:237px;top:67px;width:77px;height:83px">
      <div class="photo hall" style="height:40px" role="img" aria-label="Empty data hall"></div>
      <p style="top:47px">HKC Capital &amp; Meridian Life</p>
      <div class="btn outline" style="top:67px">Explore More</div>
    </div>
    <div class="card" style="left:316px;top:67px;width:77px;height:83px">
      <div class="photo hall" style="height:40px" role="img" aria-label="Empty data hall"></div>
      <p style="top:47px">A renowned China based Securities firm</p>
      <div class="btn outline" style="top:67px">Explore More</div>
    </div>
  </section>

  <section class="section grey" style="top:324px;height:310px">
    <div class="tag" style="top:23px"><span>Our Blogs</span></div>
    <div class="title" style="top:36px">News &amp; Events</div>
    <div class="news-item" style="top:67px">
      <div class="photo hall" style="left:145px;top:0;width:58px;height:58px" role="img" aria-label="Data center corridor"></div>
      <div class="date" style="left:210px;top:6px">23 December 2023</div>
      <h4 style="left:210px;top:14px">Title of the News or Event Post</h4>
      <p class="small" style="left:210px;top:24px;width:115px">Lorem ipsum dolor sit amet, consecter adipiscing elit. Amet proin ut vita, felis. Mauris aliquet faucibus iaculis dui vitae ullamcorper ac.</p>
      <div class="more" style="left:210px;top:45px">Read More</div>
    </div>
    <div class="abs" style="left:145px;top:130px;width:182px;height:.6px;background:#d6d8de"></div>
    <div class="news-item" style="top:135px">
      <div class="photo hall" style="left:145px;top:0;width:58px;height:58px" role="img" aria-label="Data center corridor"></div>
      <div class="date" style="left:210px;top:6px">23 December 2023</div>
      <h4 style="left:210px;top:14px">Title of the News or Event Post</h4>
      <p class="small" style="left:210px;top:24px;width:115px">Lorem ipsum dolor sit amet, consecter adipiscing elit. Amet proin ut vita, felis. Mauris aliquet faucibus iaculis dui vitae ullamcorper ac.</p>
      <div class="more" style="left:210px;top:45px">Read More</div>
    </div>
    <div class="abs" style="left:145px;top:198px;width:182px;height:.6px;background:#d6d8de"></div>
    <div class="news-item" style="top:203px">
      <div class="photo hall" style="left:145px;top:0;width:58px;height:58px" role="img" aria-label="Data center corridor"></div>
      <div class="date" style="left:210px;top:6px">23 December 2023</div>
      <h4 style="left:210px;top:14px">Title of the News or Event Post</h4>
      <p class="small" style="left:210px;top:24px;width:115px">Lorem ipsum dolor sit amet, consecter adipiscing elit. Amet proin ut vita, felis. Mauris aliquet faucibus iaculis dui vitae ullamcorper ac.</p>
      <div class="more" style="left:210px;top:45px">Read More</div>
    </div>
    <div class="btn" style="left:217px;top:276px;width:38px;height:15px">View All</div>
  </section>

  <section class="section" style="top:634px;height:140px">
    <div class="tag" style="top:32px"><span>Featured In</span></div>
    <div class="title" style="top:45px">Our <em>Partners</em></div>
    <div class="partners abs" style="left:68px;top:73px;width:336px;display:flex;justify-content:space-between;align-items:center">
      <span>Quellon</span><span>Narvik</span><span>Holtmann</span><span>Sentrava</span><span>Cabrix</span>
    </div>
    <div class="btn outline" style="left:217px;top:96px;width:38px;height:15px">View All</div>
  </section>

  <section class="section dark" style="top:774px;height:249px">
    <div class="tag left on-dark" style="left:92px;top:23px"><span>Contact Us</span></div>
    <div class="abs" style="left:92px;top:36px;font-family:'Roboto',sans-serif;font-weight:500;font-size:15px;line-height:1.3">Get in Touch<br>with Us</div>
    <p class="abs" style="left:251px;top:43px;width:132px;font-size:4px;line-height:1.5;color:#d3d6df">Lorem ipsum dolor sit amet, consectetur adipiscing elit. Amet proin ut vitae, felis. Mauris aliquet faucibus iaculis dui vitae ullamcorper ac</p>
    <svg class="abs" style="left:92px;top:81px" width="11" height="11" viewBox="0 0 11 11"><circle cx="5.5" cy="5.5" r="5.5" fill="#2c3350"/><path d="M5.5 2.6a1.9 1.9 0 0 0-1.9 1.9c0 1.4 1.9 3.6 1.9 3.6s1.9-2.2 1.9-3.6a1.9 1.9 0 0 0-1.9-1.9z" fill="#fff"/><circle cx="5.5" cy="4.5" r=".7" fill="#2c3350"/></svg>
    <p class="abs" style="left:109px;top:82px;width:110px;font-size:3.3px;line-height:1.3;color:#c4c7d2">Rm 1208, 12/F, Harbour Tech Centre, 18 Kai Fuk Road, Kowloon Bay, Hong Kong</p>
    <div class="abs" style="left:92px;top:101px;width:134px;height:83px;background:linear-gradient(135deg,#e8ecef,#d9e2dc 50%,#efe9dd)" role="img" aria-label="Street map of the office location"></div>
    <div class="field" style="top:78px;height:15px">Your name*</div>
    <div class="field" style="top:101px;height:15px">Email*</div>
    <div class="field" style="top:123px;height:15px">Subject*</div>
    <div class="field" style="top:146px;height:38px">Your Message</div>
    <div class="btn" style="left:251px;top:193px;width:38px;height:15px">Submit</div>
  </section>

  <footer class="section" style="top:1023px;height:102px;background:var(--footer);color:#fff">
    <div class="logo" style="left:12px;top:17px;font-size:9px"><i style="width:8px;height:8px"></i>Tovlen</div>
    <p class="abs" style="left:12px;top:40px;width:76px;font-size:3px;line-height:1.35;color:#a5a7ad">Lorem ipsum dolor sit amet consectetur. Mi nibh venenatis in suscipit turpis enim cursus vulputate amet. Lobortis mi platea aliquam senectus tempus mauris neque.</p>
    <div class="abs" style="left:12px;top:60px;display:flex;gap:6px">
      <i style="width:4px;height:4px;border-radius:50%;background:#fff;display:block"></i>
      <i style="width:4px;height:4px;border-radius:50%;background:#fff;display:block"></i>
      <i style="width:4px;height:4px;background:#fff;display:block"></i>
    </div>
    <div class="footer-col abs" style="left:179px;top:17px;width:60px">
      <h6>Website Links</h6><p>Home</p><p style="margin-top:8px">About Us</p><p style="margin-top:8px">Our Projects</p><p style="margin-top:8px">FAQs</p>
    </div>
    <div class="footer-col abs" style="left:255px;top:17px;width:48px">
      <h6>Services</h6><p>Website Data Centre Design &amp; Build</p><p>Structured cabling and fiber backbone</p><p>All-In-One Rack / Micro-Data Center</p><p>Audiovisual and Conference Room</p>
    </div>
    <div class="footer-col abs" style="left:349px;top:17px;width:64px">
      <h6>Contact Us</h6>
      <p style="padding-left:11px">Rm 1208, 12/F, Harbour Tech Centre, 18 Kai Fuk Road, Kowloon Bay, Hong Kong</p>
      <p style="padding-left:11px">marketing@tovlensys.com.hk</p>
      <p style="padding-left:11px">+852 3987 4100 /<br>+852 5412 7730</p>
      <p style="padding-left:11px">+852 3987 4199</p>
    </div>
    <div class="abs" style="left:12px;top:86px;width:352px;height:.5px;background:#55575d"></div>
    <div class="abs" style="left:0;top:92px;width:100%;text-align:center;font-size:3px;color:#c4c6cb">Non Copyrighted © 2022 Design and upload by Tovlen Systems</div>
  </footer>
</div>

<!-- LEFT PAGE -->
<div class="page page-left">

  <section class="section hero" style="top:0;height:233px;color:#fff">
    <div class="abs" style="left:0;top:0;width:100%;height:100%;background:linear-gradient(180deg,rgba(40,50,90,.35),rgba(20,25,60,.1))" role="img" aria-label="Server racks in a dimly lit data center"></div>
    <div class="logo" style="left:65px;top:15px;font-size:10px"><i style="width:9px;height:9px"></i>Tovlen</div>
    <div class="nav" style="left:0;width:100%">
      <span style="left:253px;color:var(--red)">Home</span>
      <span style="left:282px">About Us</span>
      <span style="left:319px">Our Services</span>
      <span style="left:362px">Our Projects</span>
      <span style="left:408px">Contact</span>
    </div>
    <div class="abs" style="left:61px;top:75px;font-size:3.5px;border-left:1px solid var(--red);padding-left:3px">The #Best Technical Solutions Provider</div>
    <h1 class="abs" style="left:61px;top:83px;font-family:'Roboto',sans-serif;font-weight:500;font-size:16.5px;line-height:20px">Design Your IT Infrastructure<br>Solution with the Best</h1>
    <p class="abs" style="left:61px;top:128px;width:196px;font-size:4.4px;line-height:1.7;color:#d4d7e2">We deliver the best in Data Center Infrastructure, Network Infrastructure, Structured Cabling, Telephony, Access Control, Video Surveillance, Audiovisual &amp; Conferencing, Relocation &amp; Migration and Maintenance solutions.</p>
    <div class="btn" style="left:61px;top:161px;width:51px;height:15px">Explore More</div>
  </section>

  <section class="section grey" style="top:233px;height:188px">
    <div class="tag" style="top:24px"><span>Why We Special</span></div>
    <div class="title" style="top:37px">Why We <em>Special</em></div>
    <div class="feature" style="left:125px;top:73px">
      <svg width="18" height="20" viewBox="0 0 18 20" fill="none" stroke="#333" stroke-width=".7"><circle cx="9" cy="9" r="5"/><circle cx="9" cy="9" r="2.5" stroke="var(--red)"/><path d="M7 14v3h4v-3M9 1v2M2 9H0M18 9h-2M3.5 3.5l1.4 1.4M14.5 3.5l-1.4 1.4"/></svg>
      <h5>Comprehensive Expertise</h5>
      <p class="small">Lorem ipsum dolor sit amet, consectetur adipiscing elit. Amet proin ut vitae, felis. Mauris aliquet faucibus iaculis dui vitae ullamcorper ac.</p>
    </div>
    <div class="feature" style="left:257px;top:73px">
      <svg width="20" height="20" viewBox="0 0 20 20" fill="none" stroke="#333" stroke-width=".7"><circle cx="10" cy="4" r="3" stroke="var(--red)"/><path d="M8.7 4l1 1 1.8-2" stroke="var(--red)"/><path d="M1 12l4-4 4 2 3-1 4 3-5 5-4-1-3-2zM19 12l-4-4"/></svg>
      <h5>Recognition &amp; Trust</h5>
      <p class="small">Lorem ipsum dolor sit amet, consectetur adipiscing elit. Amet proin ut vitae, felis. Mauris aliquet faucibus iaculis dui vitae ullamcorper ac</p>
    </div>
    <div class="feature" style="left:124px;top:123px">
      <svg width="20" height="20" viewBox="0 0 20 20" fill="none" stroke="#333" stroke-width=".7"><circle cx="10" cy="7" r="5" stroke="var(--red)"/><path d="M10 4v6M8.5 5.5h2.5a1 1 0 0 1 0 2H9a1 1 0 0 0 0 2h2.5" stroke="var(--red)"/><path d="M1 8v6l4 5M19 8v6l-4 5M4 11l3 4M16 11l-3 4"/></svg>
      <h5>Cost-Effective Solutions</h5>
      <p class="small">Lorem ipsum dolor sit amet, consectetur adipiscing elit. Amet proin ut vitae, felis. Mauris aliquet faucibus iaculis dui vitae ullamcorper ac</p>
    </div>
    <div class="feature" style="left:258px;top:123px">
      <svg width="20" height="20" viewBox="0 0 20 20" fill="none" stroke="#333" stroke-width=".7"><circle cx="10" cy="3" r="2"/><circle cx="10" cy="11" r="3.5" stroke="var(--red)"/><circle cx="10" cy="11" r="1.3" stroke="var(--red)"/><circle cx="3" cy="13" r="1.6"/><circle cx="17" cy="13" r="1.6"/><path d="M0.5 19a2.5 2.5 0 0 1 5 0M14.5 19a2.5 2.5 0 0 1 5 0M7 7l3-2 3 2"/></svg>
      <h5>Dedicated &amp; Supportive Team</h5>
      <p class="small">Lorem ipsum dolor sit amet, consectetur adipiscing elit. Amet proin ut vitae, felis. Mauris aliquet faucibus iaculis dui vitae ullamcorper ac</p>
    </div>
  </section>

  <section class="section" style="top:421px;height:173px">
    <div class="tag" style="top:34px"><span>What We Do</span></div>
    <div class="title" style="top:46px">Our Services</div>
    <div class="service active" style="left:34px">
      <b>01.</b>
      <svg class="abs" style="left:80px;top:18px" width="16" height="4" viewBox="0 0 16 4"><path d="M0 2h15M13 .5l2 1.5-2 1.5" stroke="#fff" stroke-width=".6" fill="none"/></svg>
      <p>Data Center Design &amp;<br>Build</p>
    </div>
    <div class="service" style="left:140px"><b>02.</b><p>Structured cabling &amp;<br>fiber backbone</p></div>
    <div class="service" style="left:245px"><b>03.</b><p>All-In-One Rack /<br>Micro-Data Center</p></div>
    <div class="service" style="left:350px"><b>04.</b><p>Audiovisual and<br>Conference Room</p></div>
  </section>

  <section class="section dark" style="top:594px;height:227px">
    <div class="tag left on-dark" style="left:99px;top:23px"><span>Who We Are</span></div>
    <div class="abs" style="left:99px;top:37px;font-family:'Roboto',sans-serif;font-weight:500;font-size:15.5px;line-height:20px">About<br><span style="color:var(--red)">Tovlen</span> Systems</div>
    <p class="abs" style="left:255px;top:39px;width:136px;font-size:4.3px;line-height:1.75;color:#d3d6df">We deliver the best in Data Center Infrastructure, Network Infrastructure, Structured Cabling, Telephony, Access Control, Video Surveillance, Audiovisual &amp; Conferencing, Relocation &amp; Migration and Maintenance solutions.</p>
    <div class="photo warm" style="left:99px;top:90px;width:105px;height:101px" role="img" aria-label="Miniature workers with a network cable connector"></div>
    <div class="abs" style="left:255px;top:91px;font-size:4.8px;font-weight:700">Tovlen’s solution at-a-glance includes;</div>
    <ul class="check abs" style="left:255px;top:106px">
      <li>Data Center / Server Room Design and Build</li>
      <li>Structured Cabling Solution</li>
      <li>Data and Voice Networks, IP-Telephony Solution</li>
      <li>WiFi Solution</li>
      <li>Relocation and Migration Service</li>
      <li>AV and Conference Room System</li>
    </ul>
    <div class="btn" style="left:255px;top:176px;width:51px;height:15px">Explore More</div>
  </section>

  <section class="section" style="top:821px;height:196px">
    <div class="tag" style="top:28px"><span>What We Have Done</span></div>
    <div class="title" style="top:41px">Our <em>Projects</em></div>
    <div class="card" style="left:81px;top:69px;width:79px;height:86px">
      <div class="photo hall" style="height:41px" role="img" aria-label="Empty data hall"></div>
      <p style="top:48px">A renowned China based listed insurance company</p>
      <div class="btn outline" style="top:70px">Explore More</div>
    </div>
    <div class="card active" style="left:163px;top:69px;width:79px;height:86px">
      <div class="photo hall" style="height:41px" role="img" aria-label="Empty data hall"></div>
      <p style="top:48px">Worldmart Sourcing</p>
      <div class="btn" style="top:70px">Explore More</div>
    </div>
    <div class="card" style="left:244px;top:69px;width:79px;height:86px">
      <div class="photo hall" style="height:41px" role="img" aria-label="Empty data hall"></div>
      <p style="top:48px">HKC Capital &amp; Meridian Life</p>
      <div class="btn outline" style="top:70px">Explore More</div>
    </div>
    <div class="card" style="left:326px;top:69px;width:79px;height:86px">
      <div class="photo hall" style="height:41px" role="img" aria-label="Empty data hall"></div>
      <p style="top:48px">A renowned China based Securities firm</p>
      <div class="btn outline" style="top:70px">Explore More</div>
    </div>
  </section>

  <section class="section grey" style="top:1017px;height:108px">
    <div class="tag" style="top:23px"><span>Our Blogs</span></div>
    <div class="title" style="top:36px">News &amp; Events</div>
    <div class="news-item" style="top:69px">
      <div class="photo hall" style="left:150px;top:0;width:59px;height:60px" role="img" aria-label="Data center corridor"></div>
      <div class="date" style="left:217px;top:6px">23 December 2023</div>
      <h4 style="left:217px;top:14px">Title of the News or Event Post</h4>
      <p class="small" style="left:217px;top:24px;width:118px">Lorem ipsum dolor sit amet, consecter adipiscing elit. Amet proin ut vita, felis. Mauris aliquet faucibus iaculis dui vitae</p>
    </div>
  </section>
</div>

</body>
</html>
```